my website is tabellepiece.com. (brand name is ta belle pièce) This is just a template that i have choose for. The content and the pictures are not about my business just the template.
I would like to have 4 pages for now. 1 homepage, which will be an overview for all pages, it is right now in this way. It will directly highlight my story. My website will tell an exclusive story about details which makes the difference and will make people happy with very small things. It will be art related but very stylish as well. I also want to have a event agenda on my homepage where people can see where my next event is. Page 2 my blog, where I will write weekly about mindset, lifestyle and details. Inspiration place for people who are looking for unique and exclusive approaches in life. Page 3 shop, where I will sell my stuff which is handmade and unique, it will be limited edition stuff. Mostly I will make the designs from marbling art, which I am a teacher for. (https://www.vidorastream.com/watch?v=Kq7TbWm2Xa) check this video out for more. Page 4 is book page. Here people will be able to book private or group classes for marbling art (check the video). I have already a community of more than 500 people on join ring, which will be my public as well. I wanna implement the join ring button on this page as well. to be able to track.

This is about my website. I also need a logo for my brand, which will suit my website and my goals.

I can also give you a reference website, which really like as structure and style;
https://www.brightmorrowco.com/products/the-daybook-organizer?ref=Xp4RtLm8QzVw2NbKc7HsJd9FgTy3MvEqBa6WnUoZr1LkPxYhGiCe5DsAtQfVbNj0HmRwKyXo8LcTpZaEsUv2GqDnIwMb

ta belle pièce

4 page

• I can also give you a reference website, which really like as structure and style;
• https://www.brightmorrowco.com/products/the-daybook-organizer?ref=Xp4RtLm8QzVw2NbKc7HsJd9FgTy3MvEqBa6WnUoZr1LkPxYhGiCe5DsAtQfVbNj0HmRwKyXo8LcTpZaEsUv2GqDnIwMb

```html
<!DOCTYPE html>
<html lang="en">
<head>
<meta charset="utf-8">
<title>ta belle pièce</title>
<link rel="stylesheet" href="https://fonts.googleapis.com/css2?family=Lato:wght@400;700;900&display=swap">
<style>
:root{
  --ink:#1a1a1a;
  --text:#444;
  --muted:#777;
  --line:#dcdcdc;
  --white:#fff;
  --paper:#f7f7f7;
  --marble:#ececec;
  --deep:#0f2226;
  --gold:#e0a21a;
}
*{margin:0;padding:0;box-sizing:border-box}
html,body{width:1200px;height:2503px;overflow:hidden}
body{font-family:"Lato",Arial,sans-serif;color:var(--text);background:var(--white);position:relative}
.abs{position:absolute}
/* header */
.site-header{position:absolute;left:0;top:0;width:1200px;height:109px;background:var(--white)}
.brand{position:absolute;display:flex;align-items:center;gap:12px}
.brand-dot{width:34px;height:34px;border-radius:50%;border:2px solid var(--ink)}
.brand-name{font-size:22px;font-weight:400;color:var(--ink);letter-spacing:.5px}
.header-icons{position:absolute;top:18px;left:1001px;display:flex;gap:21px}
.icon-btn{width:40px;height:40px;border-radius:50%;background:var(--ink);display:flex;align-items:center;justify-content:center}
.main-nav{position:absolute;top:74px;left:0;width:1200px}
.main-nav a{position:absolute;font-size:13px;font-weight:700;color:var(--ink);text-decoration:none;white-space:nowrap}
/* hero */
.hero{position:absolute;top:109px;left:0;width:1200px;height:490px}
.hero-title{position:absolute;left:98px;top:315px;font-size:46px;font-weight:700;letter-spacing:6px;color:var(--white)}
.btn-outline{position:absolute;border:1.5px solid var(--white);border-radius:20px;color:var(--white);font-size:13px;font-weight:700;text-transform:uppercase;display:flex;align-items:center;justify-content:center;text-decoration:none}
/* section titles */
.section-title{position:absolute;left:0;width:1200px;text-align:center;font-size:30px;font-weight:400;color:#333;letter-spacing:.5px}
/* what we do */
.services{position:absolute;top:598px;left:0;width:1200px;height:428px;background:linear-gradient(135deg,#f2f2f2,#e4e4e4 45%,#f4f4f4 70%,#e6e6e6)}
.service{position:absolute;width:260px;text-align:center}
.service svg{display:block;margin:0 auto}
.service-label{position:absolute;left:0;width:260px;font-size:14px;font-weight:700;color:#222;text-transform:uppercase}
/* products */
.product-media{position:absolute;left:98px;top:1140px;width:537px;height:456px;border:1px solid #e3e3e3;background:var(--white)}
.thumbs{position:absolute;left:35px;top:16px;display:flex;gap:14px}
.thumb{width:82px;height:80px}
.product-title{position:absolute;left:679px;top:1133px;font-size:32px;font-weight:400;color:#333;letter-spacing:1px}
.price{position:absolute;left:679px;top:1181px;font-size:19px;color:#555}
.product-copy{position:absolute;left:679px;top:1219px;width:420px;font-size:11.5px;line-height:22px;color:#555}
.rule{position:absolute;height:1px;background:var(--line)}
.stars{position:absolute;left:682px;top:1391px;display:flex;gap:1px}
.reviews{position:absolute;left:769px;top:1390px;font-size:12.5px;color:#555}
.qty{position:absolute;left:683px;top:1430px;display:flex;align-items:center;gap:14px}
.qty-box{width:38px;height:34px;border:1px solid #ccc;display:flex;align-items:center;justify-content:center;font-size:15px}
.btn{position:absolute;height:40px;display:flex;align-items:center;justify-content:center;gap:10px;font-size:14px;font-weight:700}
.btn-dark{background:var(--ink);color:var(--white)}
.btn-light{border:1.5px solid var(--ink);color:var(--ink)}
/* events */
.events{position:absolute;top:1652px;left:0;width:1200px;height:476px}
.events .section-title{left:98px;width:auto;text-align:left;color:var(--white)}
.event-text{position:absolute;left:240px;width:370px;font-size:11.5px;line-height:22px;color:#e8e8e8}
.event-meta{position:absolute;left:670px;top:2027px;display:flex;gap:28px;font-size:12px;color:#eee}
/* footer */
.site-footer{position:absolute;top:2128px;left:0;width:1200px;height:375px;background:var(--paper)}
.footer-heading{position:absolute;font-size:19px;font-weight:400;color:#333;text-transform:uppercase}
.footer-link{position:absolute;left:559px;font-size:12.5px;color:#555;display:flex;gap:18px}
.contact-item{position:absolute;left:878px;font-size:12.5px;color:#555;display:flex;gap:18px;align-items:center}
.footer-about{position:absolute;left:98px;top:2273px;width:330px;font-size:12px;line-height:22px;color:#666}
.copyright{position:absolute;left:0;width:1200px;top:2462px;text-align:center;font-size:11.5px;color:#666}
</style>
</head>
<body>

<header class="site-header">
  <div class="brand" style="left:100px;top:34px">
    <span class="brand-dot"></span><span class="brand-name">ta belle pièce</span>
  </div>
  <div class="header-icons">
    <span class="icon-btn"><svg width="14" height="14" viewBox="0 0 14 14"><path d="M1 2h2l2 7h7l1.5-5H4" fill="none" stroke="#fff" stroke-width="1.6"/><circle cx="6" cy="12" r="1.2" fill="#fff"/><circle cx="11" cy="12" r="1.2" fill="#fff"/></svg></span>
    <span class="icon-btn"><svg width="12" height="14" viewBox="0 0 12 14"><circle cx="6" cy="4" r="3" fill="#fff"/><path d="M0 14c0-4 2.5-6 6-6s6 2 6 6z" fill="#fff"/></svg></span>
  </div>
  <nav class="main-nav">
    <a href="#" style="left:772px">Home</a>
    <a href="#" style="left:868px">My Blog</a>
    <a href="#" style="left:977px">Shop</a>
    <a href="#" style="left:1068px">Book</a>
  </nav>
</header>

<section class="hero">
  <div role="img" aria-label="Marbling tray with floating paint shapes surrounded by jars of colour" class="abs" style="inset:0;background:radial-gradient(ellipse at 50% 55%,#3a3a3a,#1c1c1c 60%,#111),linear-gradient(#555,#222)"></div>
  <svg class="abs" style="left:0;bottom:0" width="1200" height="90" viewBox="0 0 1200 90" preserveAspectRatio="none">
    <path d="M0 90 L0 88 Q600 40 1200 0 L1200 90 Z" fill="#777"/>
    <path d="M0 90 Q600 50 1200 14 L1200 90 Z" fill="#f1f1f1"/>
  </svg>
  <h1 class="hero-title" style="top:206px">Ta Belle Pièce</h1>
  <a class="btn-outline" href="#" style="left:98px;top:298px;width:136px;height:38px">Shop Now</a>
</section>

<section class="services">
  <h2 class="section-title" style="top:38px">• WHAT WE DO •</h2>
  <div class="service" style="left:84px;top:110px">
    <svg width="164" height="184" viewBox="0 0 164 184"><polygon points="82,2 162,47 162,137 82,182 2,137 2,47" fill="#fff"/>
      <path d="M82 62c-20 0-34 14-34 30s12 30 30 30c8 0 8-8 4-12s0-10 6-10h10c10 0 18-8 18-16 0-14-14-22-34-22z" fill="#111"/>
      <circle cx="66" cy="84" r="5" fill="#fff"/><circle cx="80" cy="74" r="5" fill="#fff"/><circle cx="96" cy="78" r="5" fill="#fff"/><circle cx="64" cy="102" r="5" fill="#fff"/></svg>
    <div class="service-label" style="top:205px">Marble Painting</div>
  </div>
  <div class="service" style="left:341px;top:150px">
    <svg width="164" height="184" viewBox="0 0 164 184"><polygon points="82,2 162,47 162,137 82,182 2,137 2,47" fill="#fff"/>
      <path d="M54 62l56 56M110 62l-56 56" stroke="#111" stroke-width="9"/><circle cx="104" cy="112" r="11" fill="#111"/><circle cx="104" cy="112" r="4" fill="#fff"/></svg>
    <div class="service-label" style="top:206px">Vivamus Sodales</div>
  </div>
  <div class="service" style="left:596px;top:110px">
    <svg width="164" height="184" viewBox="0 0 164 184"><polygon points="82,2 162,47 162,137 82,182 2,137 2,47" fill="#fff"/>
      <rect x="44" y="58" width="66" height="22" rx="3" fill="#111"/><path d="M110 68h8v22H80v12" fill="none" stroke="#111" stroke-width="5"/><rect x="73" y="100" width="14" height="30" rx="3" fill="#111"/></svg>
    <div class="service-label" style="top:205px">Cras Sagittis Sodales</div>
  </div>
  <div class="service" style="left:853px;top:150px">
    <svg width="164" height="184" viewBox="0 0 164 184"><polygon points="82,2 162,47 162,137 82,182 2,137 2,47" fill="#fff"/>
      <path d="M44 120L76 64l38 56z" fill="#111"/><path d="M68 78l8-14 8 14-8 6z" fill="#fff"/></svg>
    <div class="service-label" style="top:206px">Aliquam Non Accumsan</div>
  </div>
</section>

<h2 class="section-title" style="top:1064px">• OUR PRODUCTS •</h2>
<div class="product-media">
  <div role="img" aria-label="Marbled paper sheets with paint bottles and brushes on a wooden table" class="abs" style="left:0;top:0;width:535px;height:338px;background:linear-gradient(135deg,#cfcac2,#a7a39c 40%,#e0a34a 70%,#e3c04a)"></div>
  <div class="thumbs" style="top:355px">
    <div class="thumb" role="img" aria-label="Marbling workshop thumbnail" style="background:linear-gradient(135deg,#5b4a3a,#c9b54a)"></div>
    <div class="thumb" role="img" aria-label="Pink marbled design thumbnail" style="background:linear-gradient(135deg,#2a2a3a,#d94a8a)"></div>
    <div class="thumb" role="img" aria-label="Marbling tray thumbnail" style="background:linear-gradient(135deg,#222,#6b6b6b)"></div>
    <div class="thumb" role="img" aria-label="Flower marbling thumbnail" style="background:linear-gradient(135deg,#4a3a4a,#b98aa0)"></div>
    <div class="thumb" role="img" aria-label="Teal marbled paper thumbnail" style="background:linear-gradient(135deg,#7a9a8a,#c9a06a)"></div>
  </div>
  <svg class="abs" style="left:8px;top:380px" width="12" height="20"><path d="M10 2L3 10l7 8" fill="none" stroke="#333" stroke-width="2"/></svg>
  <svg class="abs" style="right:8px;top:380px" width="12" height="20"><path d="M2 2l7 8-7 8" fill="none" stroke="#333" stroke-width="2"/></svg>
</div>
<h3 class="product-title">MARBLE&nbsp; ARTWORK</h3>
<div class="price">$24.95 USD</div>
<p class="product-copy">Lorem ipsum dolor sit amet, consectetur adipiscing elit. Donec aliquet arcu a quam ultrices vestibulum. Integer euismod, diam vitae dapibus pharetra, neque odio laoreet turpis, id iaculis dolor metus eu eros. In lacus velit, imperdiet eu dui id, molestie efficitur justo. Vestibulum vitae nibh ultrices, commodo dui ut, iaculis metus. Aliquam dui urna,</p>
<div class="rule" style="left:679px;top:1365px;width:422px"></div>
<div class="stars">
  <svg width="72" height="13" viewBox="0 0 72 13"><g fill="#c98a16"><path id="s" d="M6.5 0l2 4.3 4.5.5-3.4 3 1 4.6-4.1-2.4-4.1 2.4 1-4.6L0 4.8l4.5-.5z"/><use href="#s" x="14.5"/><use href="#s" x="29"/><use href="#s" x="43.5"/><use href="#s" x="58"/></g></svg>
</div>
<div class="reviews">156 Reviews</div>
<div class="qty">
  <svg width="14" height="4"><rect width="14" height="4" fill="#222"/></svg>
  <div class="qty-box">1</div>
  <svg width="14" height="14"><path d="M7 0v14M0 7h14" stroke="#222" stroke-width="3"/></svg>
</div>
<div class="btn btn-dark" style="left:684px;top:1490px;width:146px">
  <svg width="14" height="13" viewBox="0 0 14 14"><path d="M1 2h2l2 7h7l1.5-5H4" fill="none" stroke="#fff" stroke-width="1.6"/><circle cx="6" cy="12" r="1.2" fill="#fff"/><circle cx="11" cy="12" r="1.2" fill="#fff"/></svg>Add To Cart</div>
<div class="btn btn-light" style="left:855px;top:1490px;width:146px">
  <svg width="14" height="13" viewBox="0 0 14 13"><path d="M7 12L1.5 6.5A3.2 3.2 0 0 1 7 2a3.2 3.2 0 0 1 5.5 4.5z" fill="#111"/></svg>My Wishlist</div>

<section class="events">
  <div role="img" aria-label="Dark green marbled background with gold veins" class="abs" style="inset:0;background:radial-gradient(ellipse at 20% 40%,#1f3a3c,transparent 55%),radial-gradient(ellipse at 85% 70%,#4a3a1c,transparent 45%),var(--deep)"></div>
  <svg class="abs" style="left:0;bottom:-1px" width="1200" height="70" viewBox="0 0 1200 70" preserveAspectRatio="none"><path d="M0 70V40Q600 -10 1200 40V70Z" fill="#f7f7f7"/></svg>
  <h2 class="section-title" style="top:32px">• UPCOMING EVENTS •</h2>
  <div role="img" aria-label="Painter working on a marbled canvas" class="abs" style="left:98px;top:116px;width:122px;height:112px;border:1px solid #ccc;background:linear-gradient(135deg,#6a5a4a,#c9b04a)"></div>
  <p class="event-text" style="top:112px">Cras sagittis sodales nunc, sed suscipit erat imperdiet eu. Sed pretium metus sit amet velit congue, ac lobortis elit efficitur. Etiam sagittis erat eget mi tristique mattis. Phasellus enim metus</p>
  <a class="btn-outline" href="#" style="left:247px;top:196px;width:120px;height:32px;text-transform:none">Learn More &gt;&gt;</a>
  <div role="img" aria-label="Outdoor café table with a coffee cup" class="abs" style="left:98px;top:279px;width:122px;height:110px;border:1px solid #ccc;background:linear-gradient(180deg,#b9c4cc,#8a8a8a 55%,#9a2a2a)"></div>
  <p class="event-text" style="top:275px">Cras sagittis sodales nunc, sed suscipit erat imperdiet eu. Sed pretium metus sit amet velit congue, ac lobortis elit efficitur. Etiam sagittis erat eget mi tristique mattis. Phasellus enim metus</p>
  <a class="btn-outline" href="#" style="left:247px;top:358px;width:120px;height:32px;text-transform:none">Learn More &gt;&gt;</a>
  <div role="img" aria-label="Artist marbling a large canvas at a workshop table" class="abs" style="left:649px;top:110px;width:453px;height:300px;border:1px solid #ccc;background:linear-gradient(135deg,#8a6a5a,#4a3a2a 45%,#8a8a2a 75%,#5a5a4a)"></div>
  <div class="event-meta" style="top:375px">
    <span><svg width="10" height="11" viewBox="0 0 12 14"><circle cx="6" cy="4" r="3" fill="#eee"/><path d="M0 14c0-4 2.5-6 6-6s6 2 6 6z" fill="#eee"/></svg>&nbsp; By Someone</span>
    <span><svg width="12" height="11" viewBox="0 0 12 11"><path d="M1 1h10v6H5l-3 3V7H1z" fill="#eee"/></svg>&nbsp; 23 Comments</span>
  </div>
</section>

<footer class="site-footer">
  <div class="brand" style="left:98px;top:116px">
    <span class="brand-dot"></span><span class="brand-name">ta belle pièce</span>
  </div>
  <p class="footer-about" style="top:145px">Cras sagittis sodales nunc, sed suscipit erat imperdiet eu. Sed pretium metus sit amet velit congue, ac lobortis elit efficitur. Etiam sagittis erat eget mi tristique mattis. Phasellus enim</p>
  <h4 class="footer-heading" style="left:559px;top:49px">Important Links</h4>
  <h4 class="footer-heading" style="left:878px;top:49px">Contact Us</h4>
  <div class="footer-link" style="top:97px"><span>»</span>Our Products</div>
  <div class="rule" style="left:559px;top:136px;width:175px"></div>
  <div class="footer-link" style="top:151px"><span>»</span>Best Customer Reviews</div>
  <div class="rule" style="left:559px;top:189px;width:175px"></div>
  <div class="footer-link" style="top:204px"><span>»</span>Locations</div>
  <div class="rule" style="left:559px;top:242px;width:175px"></div>
  <div class="footer-link" style="top:257px"><span>»</span>What We Do</div>
  <div class="contact-item" style="top:97px"><svg width="9" height="13" viewBox="0 0 9 13"><path d="M4.5 0A4.5 4.5 0 0 0 0 4.5C0 8 4.5 13 4.5 13S9 8 9 4.5A4.5 4.5 0 0 0 4.5 0z" fill="#444"/><circle cx="4.5" cy="4.5" r="1.7" fill="#f7f7f7"/></svg>Harbour Lane, Eastport</div>
  <div class="contact-item" style="top:151px"><svg width="12" height="12" viewBox="0 0 12 12"><path d="M2 0l2.5 3-1.3 1.6a8 8 0 0 0 4.2 4.2L9 7.5 12 10l-2 2C4.5 12 0 7.5 0 2z" fill="#444"/></svg>0851234967</div>
  <div class="contact-item" style="top:204px"><svg width="13" height="10" viewBox="0 0 13 10"><rect width="13" height="10" fill="#444"/><path d="M0 0l6.5 5L13 0" fill="none" stroke="#f7f7f7" stroke-width="1.2"/></svg>info@tabellepiece.com</div>
  <div class="abs" style="left:878px;top:237px;display:flex;gap:14px">
    <span style="width:13px;height:13px;border-radius:50%;background:#444;display:block"></span>
    <span style="width:13px;height:13px;border-radius:50%;background:#444;display:block"></span>
  </div>
  <div class="rule" style="left:98px;top:312px;width:1004px"></div>
  <div class="copyright" style="top:334px">Copyright © 2017 ta belle pièce - All Rights Reserved.</div>
</footer>

</body>
</html>
```